Wordpress Design Project

Word press design for speaker/writer to blog and let audience know what I'm doing, who I am and what my message is about.
I've written a couple of books and intend to promote my books, articles/blogs and video blogs on this site.
I would like to have an about me tab, rotating pictures in the header, (not sure I'm describing that correctly, but the following is a link that shows you what I mean) :
http://velmostra.com/simplymarla/2013/01/30/hello-world/
I'd like to have the share this buttons for all the social media sites (probably a widget?), as well as the stats on how often the link, video or article was shared.
Updates
Project Deadline Extended
Reason: My timeframes have been moved out because the marketing media event that caused me to need this site immediately has been moved out a couple of days. Hopeully there is more time to have more designers submit now.
Target Market(s)
Mainly women 30+
Industry/Entity Type
Media
Requirements
Must have
- My Simply Marla logo needs to be on the site and I'd like to have the share this buttons for all the social media sites (probably a widget?), as well as the stats on how often the link, video or article was shared. I'd like to be able to see the comments and be able to maintain the site myself as well as swap out the pictures if I so desire.
I added files, but they are png, let me know if you need the ai files.
I'd like to be able to add tabs later if I decide so I'd like the template to be flexible enough that I can add a tab without compromising the look and feel of the site.
I also want to be able to upload my videos to the site.

```html
<!DOCTYPE html>
<html lang="en">
<head>
<meta charset="utf-8">
<title>Simply Marla — Unveiling My Authentic Voice</title>
<link rel="stylesheet" href="https://fonts.googleapis.com/css2?family=Arimo:wght@400;700&display=swap">
<style>
  :root {
    --canvas-bg: #ececec;
    --page-white: #ffffff;
    --ink-dark: #1e2a31;
    --ink-body: #3b3f42;
    --ink-muted: #6a6f73;
    --nav-dark-top: #3c474c;
    --nav-dark-bottom: #232c30;
    --nav-tab: #56656c;
    --nav-tab-active: #f2f4f5;
    --accent-cyan: #2fb6d6;
    --hero-teal: #248ca2;
    --hero-frame: #5fb4c6;
    --rule: #d8dde0;
    --column-line: #e3e7e9;
    --footer-bg: #dfe5e8;
    --rss: #ee7a1f;
    --chirp: #5fc6ea;
    --circle: #3b5a98;
    --reel: #c6211f;
    --button-top: #3a3f42;
    --button-bottom: #14181a;
  }
  * { margin: 0; padding: 0; box-sizing: border-box; }
  html, body {
    width: 900px; height: 1200px; overflow: hidden;
    background: var(--canvas-bg);
    font-family: "Arimo", Arial, sans-serif;
  }
  .site {
    position: absolute; left: 68px; top: 62px;
    width: 766px; height: 723px;
    background: var(--page-white);
    box-shadow: 0 2px 6px rgba(0,0,0,.12);
  }
  .site > * { position: absolute; }

  /* header */
  .brand { left: 56px; top: 28px; }
  .brand-name {
    font-size: 21px; font-weight: 700; color: var(--ink-dark);
    letter-spacing: .5px; line-height: 1;
  }
  .brand-tagline {
    margin-top: 6px; font-size: 7.5px; font-weight: 700;
    color: var(--ink-dark); letter-spacing: .4px;
  }

  /* navigation */
  .main-nav {
    left: 0; top: 66px; width: 766px; height: 38px;
    background: linear-gradient(var(--nav-dark-top), var(--nav-dark-bottom));
    border-bottom: 2px solid var(--accent-cyan);
  }
  .main-nav ul { list-style: none; position: absolute; left: 56px; top: 8px; display: flex; gap: 6px; }
  .main-nav li {
    height: 30px; padding: 0 16px; line-height: 30px;
    background: var(--nav-tab); color: #fff;
    font-size: 11px; font-weight: 700; letter-spacing: .2px;
  }
  .main-nav li.is-active { background: var(--nav-tab-active); color: var(--ink-body); }

  /* hero */
  .hero {
    left: 0; top: 106px; width: 766px; height: 304px;
    background: var(--hero-teal);
  }
  .hero-frame {
    position: absolute; left: 54px; top: 8px; width: 662px; height: 283px;
    border: 1px solid var(--hero-frame);
  }
  .hero-photo {
    position: absolute; left: 0; top: 0; width: 424px; height: 281px;
    background: linear-gradient(135deg, #6f8f3c 0%, #a9b872 30%, #d7dccf 55%, #8a6a48 80%, #3d4a2a 100%);
  }
  .slider-dots { position: absolute; left: 194px; top: 270px; display: flex; gap: 3px; }
  .slider-dots span { width: 6px; height: 6px; border-radius: 50%; background: #9aa3a6; }
  .slider-dots span.is-current { background: #ffffff; }

  .about { position: absolute; left: 437px; top: 14px; width: 225px; color: #fff; }
  .about h1 { font-size: 24px; font-weight: 700; color: var(--ink-dark); line-height: 1.1; }
  .about hr { border: 0; border-top: 1px solid #7fc6d6; margin: 15px 0 8px; }
  .about p { font-size: 9.4px; line-height: 10.6px; text-align: justify; }
  .about p.lead { font-weight: 700; margin-bottom: 8px; }
  .learn-more {
    position: absolute; left: 0; top: 202px; width: 87px; height: 23px;
    background: linear-gradient(var(--button-top), var(--button-bottom));
    border-radius: 2px; color: #dfe3e4;
    font-size: 9.5px; font-weight: 700; text-align: center; line-height: 23px;
  }

  /* columns */
  .content-columns { left: 54px; top: 410px; width: 662px; height: 278px; }
  .column {
    position: absolute; top: 0; height: 278px;
    border-left: 1px solid var(--column-line);
    padding: 20px 6px 0;
  }
  .column:last-child { border-right: 1px solid var(--column-line); }
  .column h2 {
    font-size: 13px; font-weight: 700; color: var(--accent-cyan);
    text-align: center; letter-spacing: .3px;
    padding-bottom: 8px; border-bottom: 1px solid var(--rule);
  }
  .col-blogs { left: 0; width: 142px; }
  .col-news { left: 142px; width: 156px; }
  .col-video { left: 298px; width: 236px; }
  .col-connect { left: 534px; width: 128px; }

  .blog-list { list-style: none; margin-top: 10px; }
  .blog-list li {
    font-size: 9px; color: var(--ink-body); height: 17.3px; line-height: 15px;
    padding-left: 16px; position: relative;
  }
  .blog-list li::before {
    content: ""; position: absolute; left: 4px; top: 5px;
    width: 6px; height: 5px; border-left: 1px solid var(--accent-cyan);
    background: linear-gradient(135deg, transparent 45%, var(--accent-cyan) 46%, var(--accent-cyan) 56%, transparent 57%) right/4px 5px no-repeat;
  }

  .news-item { margin-top: 8px; }
  .news-item p, .video-caption {
    font-size: 9px; line-height: 10.8px; color: var(--ink-body);
  }
  .read-more { display: block; font-size: 9px; color: var(--accent-cyan); margin-top: 7px; }

  .video-still {
    margin-top: 8px; width: 215px; height: 141px;
    background: linear-gradient(180deg, #e9eef1 0%, #c9d2d8 40%, #4a4d54 75%, #2b2d33 100%);
  }
  .video-caption { margin-top: 11px; }

  .connect-list { list-style: none; margin-top: 8px; }
  .connect-list li { display: flex; align-items: center; height: 52px; }
  .connect-mark { width: 42px; height: 42px; border-radius: 3px; flex: none; }
  .connect-list span { font-size: 9px; color: var(--accent-cyan); margin-left: 7px; }
  .mark-rss { background: var(--rss); }
  .mark-chirp { background: var(--chirp); }
  .mark-circle { background: var(--circle); }
  .mark-reel { background: var(--reel); }

  /* footer */
  .site-footer {
    left: 0; top: 688px; width: 766px; height: 35px;
    background: var(--footer-bg); color: var(--ink-muted);
    font-size: 9px; text-align: center; line-height: 35px;
  }
</style>
</head>
<body>
  <div class="site">
    <header class="brand">
      <div class="brand-name">SIMPLY MARLA</div>
      <div class="brand-tagline">UNVEILING MY AUTHENTIC VOICE</div>
    </header>

    <nav class="main-nav">
      <ul>
        <li class="is-active">HOME</li>
        <li>BLOG</li>
        <li>NEWS</li>
        <li>CONTACT US</li>
      </ul>
    </nav>

    <section class="hero">
      <div class="hero-frame">
        <div class="hero-photo" role="img" aria-label="Rotating header photo: two hikers with backpacks reading a map in a sunny forest"></div>
        <div class="slider-dots"><span></span><span></span><span></span><span class="is-current"></span></div>
        <div class="about">
          <h1>About Me</h1>
          <hr>
          <p class="lead">Lorem ipsum dolor sit amet, consectetuer adipiscing elit, sed diam nonummy nibh euismod tincidunt ut laoreet dolore magna aliquam erat volutpat. Ut wisi enim ad minim veniam, quis nostrud exerci tation ullamcorper suscipit lobortis nisl ut aliquip ex ea commodo consequat.</p>
          <p>Duis autem vel eum iriure dolor in hendrerit in vulputate velit esse molestie consequat, vel illum dolore eu feugiat nulla facilisis at vero eros et accumsan et iusto odio dignissim qui blandit praesent luptatum zzril delenit augue duis dolore te feugait nulla facilisi.</p>
          <div class="learn-more">LEARN MORE</div>
        </div>
      </div>
    </section>

    <section class="content-columns">
      <div class="column col-blogs">
        <h2>BLOGS</h2>
        <ul class="blog-list">
          <li>Nulla blandit</li>
          <li>Duis ut neque lacus</li>
          <li>Aliquam pretium venenatis</li>
          <li>Nulla vitae neque ut augue</li>
          <li>Nullam tincidunt leo</li>
          <li>Suspendisse luctus</li>
          <li>Pellentesque ut tortor nibh</li>
          <li>Proin sit amet metus diam</li>
          <li>Praesent varius porta eros</li>
          <li>Vestibulum est lectus</li>
          <li>Fermentum sed pulvina</li>
        </ul>
      </div>

      <div class="column col-news">
        <h2>NEWS</h2>
        <div class="news-item">
          <p>Curabitur bibendum, ipsum sed dignissim aliquam, arcu odio mattis elit, et sagittis risus est a mi. Quisque ut venenatis dui.</p>
          <span class="read-more">Read more</span>
        </div>
        <div class="news-item">
          <p>Praesent molestie laoreet imperdiet. Class aptent taciti sociosqu ad litora torquent per conubia nostra, per inceptos himenaeos.</p>
          <span class="read-more">Read more</span>
        </div>
        <div class="news-item">
          <p>Nunc ultricies tincidunt elit eu ullamcorper. Vestibulum luctus ullamcorper accumsan. Cras tincidunt, nisl in laoreet.</p>
          <span class="read-more">Read more</span>
        </div>
      </div>

      <div class="column col-video">
        <h2>VIDEO</h2>
        <div class="video-still" role="img" aria-label="Video still: a group of business people in suits standing in a bright office"></div>
        <p class="video-caption">Vestibulum luctus ullamcorper accumsan. Cras tincidunt, nisl in laoreet tempus, diam nisi lobortis risus, sed tristique sapien arcu at tortor. Mauris lobortis facilisis justo id bibendum.</p>
        <span class="read-more">Read more</span>
      </div>

      <div class="column col-connect">
        <h2>CONNECTIONS</h2>
        <ul class="connect-list">
          <li><div class="connect-mark mark-rss"></div><span>RSS</span></li>
          <li><div class="connect-mark mark-chirp"></div><span>Chirpline</span></li>
          <li><div class="connect-mark mark-circle"></div><span>Circlepage</span></li>
          <li><div class="connect-mark mark-reel"></div><span>Reelcast</span></li>
        </ul>
      </div>
    </section>

    <footer class="site-footer">Copyright © 2013. All Rights Reserved.</footer>
  </div>
</body>
</html>
```